Interior Design & Furniture E commerce Website Design

I need a cutting edge website design, this is for Interior Design Services as well as eCommerce for furniture and home decor www.lorivelhomestudio.com
Here is a sample of the concept behind the site.
I am a furniture & Interior Designer, want to create a life style brand.
Will offer Interior Design Services : Commercial & Residential (this portion will be a catalog or portfolio type)
The eCommerce side will sell, Furniture, Lighting, Decor, Gifts, Textiles, will also be offering trade so that could be at bottom of site. I also like the concept of concierge as where all the info falls under: shipping, etc..

*Please make sure to make the eCommerce prominent.

Hello Designers, I also would like to possibly update my logo, the current one I like but don't Love.

Target Market(s)

High end customers with disposable income, who also appreciate quality and unique furniture & design

Number of Pages Required

5+ page

Colors
0255a3
f37122

Requirements
Must have
• Room Planer: I will be using this tool http://qtstudio.varnelbex.com/room-planner.inc
• Live Chat
• Will be offering 3d renderings for spaces as well as Virtual Reality
• The image I loaded that looks like copper, I would like to have that as a color on the site with the texture: so the colors are Blue and copper. Would like the site to be user friendly and interactive
• http://qtstudio.varnelbex.com/ (this is the current site in development, so we will be offering Design your own, Trends, inspiration, etc...
• I have included a headshot to use for now about me. or about us.
• I also included several actual project installation (residential and commercial) as well as a variety of my furniture items
• I have Included an old Bio and some articles I would like to show case in a Press Area
• I would also like to include a section for Events (Giving back )I do a lot of charity events 1-2 a year and would like to showcase that as well
• *Please make the store (ecommerce prominent )

```html
<!DOCTYPE html>
<html lang="en">
<head>
<meta charset="utf-8">
<title>Lorivel Home Studio</title>
<link href="https://fonts.googleapis.com/css2?family=Archivo+Narrow:wght@400;600;700&family=Open+Sans:wght@400;600;700&display=swap" rel="stylesheet">
<style>
:root{
  --blue:#0255a3;
  --orange:#f37122;
  --copper:#b5713f;
  --ink:#1d1d1d;
  --text:#555;
  --topbar:#3a3634;
  --footer:#2d2c2c;
  --footer-text:#8a8a8a;
  --soft:#f5f5f5;
  --line:#d9d9d9;
}
*{margin:0;padding:0;box-sizing:border-box}
html,body{width:1200px;height:2347px;overflow:hidden}
body{position:relative;background:#fff;font-family:"Open Sans",Arial,sans-serif;color:var(--text)}
.abs{position:absolute}
.narrow{font-family:"Archivo Narrow","Arial Narrow",sans-serif}

/* header */
.topbar{left:0;top:0;width:1200px;height:37px;background:var(--topbar)}
.hero{left:0;top:37px;width:1200px;height:523px;background:linear-gradient(100deg,#5e564b 0%,#7c6f5d 30%,#8c9a96 55%,#6f8a6a 75%,#4c5a48 100%)}
.hero-shade{left:0;top:37px;width:1200px;height:523px;background:rgba(20,18,15,.35)}
.brand-plate{left:0;top:0;width:344px;height:119px}
.brand{left:150px;top:42px;font-family:"Archivo Narrow",sans-serif;font-size:22px;letter-spacing:2px;color:var(--copper);font-weight:400;display:flex;align-items:center;gap:10px}
.brand .mark{width:14px;height:14px;background:var(--copper)}
.nav{left:572px;top:70px;display:flex;gap:0;font-family:"Archivo Narrow",sans-serif;font-weight:700;font-size:12px;color:#fff;letter-spacing:.3px}
.nav span{margin-right:40px}
.cart{left:1011px;top:8px}
.cart-count{left:1006px;top:4px;width:12px;height:12px;border-radius:50%;background:var(--orange);color:#fff;font-size:7px;text-align:center;line-height:12px}
.hero-rule{left:300px;width:600px;height:2px;background:#fff}
.hero-title{left:0;top:300px;width:1200px;text-align:center;font-family:"Archivo Narrow",sans-serif;font-weight:600;font-size:36px;line-height:44px;color:#fff}

/* about */
.about{left:0;top:560px;width:1200px;height:968px;background:var(--soft)}
.divider{left:0;width:1200px;height:1px;background:var(--line)}
.divider-mark{width:40px;height:40px;left:580px;background:var(--soft);display:flex;align-items:center;justify-content:center}
.divider-mark i{display:block;width:30px;height:30px;border:1.5px solid var(--copper);opacity:.7}
.about-title{left:0;top:654px;width:1200px;text-align:center;font-family:"Archivo Narrow",sans-serif;font-weight:700;font-size:32px;color:var(--ink)}
.about-lead{left:0;top:698px;width:1200px;text-align:center;font-family:"Archivo Narrow",sans-serif;font-size:14px;color:#333}
.about-copy{left:200px;top:738px;width:800px;text-align:center;font-size:11px;line-height:17px;color:#555}

/* shop */
.tab{top:914px;height:31px;border:1px solid #d6d6d6;background:#fff;font-family:"Archivo Narrow",sans-serif;font-weight:700;font-size:11px;color:#333;display:flex;align-items:center;justify-content:center}
.tab.active{background:var(--orange);border-color:var(--orange);color:#fff}
.product{width:180px;height:161px}
.chairs-overlay{width:180px;height:161px;background:#f1f1f1}
.chairs-label{color:#fff;font-family:"Archivo Narrow",sans-serif;font-weight:700;font-size:12px;text-align:center;width:80px;line-height:26px}
.bag-btn{width:27px;height:27px;border:1px solid #bbb;background:#fff;display:flex;align-items:center;justify-content:center}
.price{width:62px;height:27px;border:1px solid #bbb;background:#fff;font-family:"Archivo Narrow",sans-serif;font-weight:700;font-size:12px;color:#222;display:flex;align-items:center;justify-content:center}

/* profile */
.portrait{left:0;top:1528px;width:310px;height:348px}
.section-title{font-family:"Archivo Narrow",sans-serif;font-weight:700;font-size:32px;color:var(--ink)}
.section-sub{font-family:"Archivo Narrow",sans-serif;font-size:14px;color:#333}
.card{border:1px solid #ddd;background:#fff}
.bio{left:363px;top:1672px;width:372px;height:143px;padding:20px 30px;font-size:10.5px;line-height:17px;color:#555}
.design-card{left:821px;top:1672px;width:216px;height:143px}
.design-btn{left:846px;width:168px;height:34px;color:#fff;font-family:"Archivo Narrow",sans-serif;font-weight:700;font-size:11px;display:flex;align-items:center;justify-content:center}

/* press band */
.press{left:0;top:1876px;width:1200px;height:242px;background:var(--blue)}
.press-copy{left:200px;top:1931px;width:800px;text-align:center;color:#fff;font-size:10.5px;line-height:17px}
.press-date{left:0;top:1993px;width:1200px;text-align:center;color:#fff;font-family:"Archivo Narrow",sans-serif;font-weight:700;font-size:12px}
.press-btn{left:538px;top:2029px;width:122px;height:36px;border:2px solid #fff;color:#fff;font-family:"Archivo Narrow",sans-serif;font-weight:700;font-size:11px;display:flex;align-items:center;justify-content:center}

/* footer */
.footer{left:0;top:2118px;width:1200px;height:229px;background:var(--footer)}
.foot-head{top:2160px;font-family:"Archivo Narrow",sans-serif;font-weight:700;font-size:13px;color:#fff}
.foot-links{top:2186px;font-size:10px;line-height:17px;color:var(--footer-text);list-style:none}
.foot-links li::before{content:"- ";}
.foot-links .current{color:var(--orange)}
.news-input{left:483px;top:2192px;width:213px;height:34px;background:#4a4949}
.news-submit{left:483px;top:2232px;width:85px;height:35px;background:var(--orange);color:#fff;font-family:"Archivo Narrow",sans-serif;font-weight:700;font-size:11px;display:flex;align-items:center;justify-content:center}
.event{left:738px;top:2186px;width:300px;font-size:10px;line-height:15px;color:#6d6d6d}
.event b{color:var(--orange)}
.foot-rule{left:163px;top:2297px;width:875px;height:1px;background:#444}
.copyright{left:163px;top:2316px;font-size:9px;color:#6d6d6d}
.social{top:2309px;width:27px;height:27px}
</style>
</head>
<body>

<!-- header -->
<div class="abs hero" role="img" aria-label="Photo of a luxury covered patio with lounge sofas overlooking a pool and palm-lined landscape"></div>
<div class="abs hero-shade"></div>
<div class="abs topbar"></div>
<svg class="abs brand-plate" viewBox="0 0 344 119" aria-hidden="true"><polygon points="0,0 344,0 300,119 0,119" fill="#fff"/></svg>
<div class="abs brand"><span class="mark"></span>LORIVEL</div>
<nav class="abs nav"><span>HOME</span><span>ABOUT US</span><span>OUR SERVICES</span><span>SHOP</span><span>CONTACT US</span><span>BLOG</span></nav>
<svg class="abs cart" width="28" height="24" viewBox="0 0 28 24" aria-hidden="true"><rect x="1" y="1" width="26" height="22" fill="none" stroke="#cfcfcf" stroke-width="1.5"/><path d="M9 9h10l-1 9H10z" fill="#cfcfcf"/><path d="M11 9a3 3 0 0 1 6 0" fill="none" stroke="#cfcfcf" stroke-width="1.3"/></svg>
<div class="abs cart-count">0</div>
<div class="abs hero-rule" style="top:288px"></div>
<h1 class="abs hero-title">Lorivel Home Studio is a full service<br>interior design firm</h1>
<div class="abs hero-rule" style="top:404px"></div>

<!-- about -->
<section class="abs about"></section>
<div class="abs divider" style="top:613px"></div>
<div class="abs divider-mark" style="top:593px"><i></i></div>
<h2 class="abs about-title">About Lorivel Design</h2>
<p class="abs about-lead">Lorivel Home Studio is a full service interior design firm led by principal designer Lori Velasco-Hart.</p>
<p class="abs about-copy">As a child, Lori would spend quality time with her Father by helping out in his furniture manufacturing company. She was delighted to be taken along on project installations to exciting places like the Solenne and other high-end hotels. What began as a fun after-school activity evolved into a passion for furniture &amp; interior design and quality materials.</p>
<div class="abs divider" style="top:829px"></div>
<div class="abs divider-mark" style="top:809px"><i></i></div>

<!-- shop tabs -->
<div class="abs tab active" style="left:355px;width:85px">FURNITURE</div>
<div class="abs tab" style="left:455px;width:86px">LIGHTING</div>
<div class="abs tab" style="left:555px;width:85px">DECOR</div>
<div class="abs tab" style="left:655px;width:87px">GIFTS</div>
<div class="abs tab" style="left:757px;width:85px">TEXTILES</div>

<!-- products row 1 -->
<div class="abs product" style="left:203px;top:984px;background:linear-gradient(160deg,#4c5a3a,#8a7256 55%,#3a2c22)" role="img" aria-label="Photo of a tufted footstool with gilded legs in a garden room"></div>
<div class="abs chairs-overlay" style="left:408px;top:984px;box-shadow:0 1px 4px rgba(0,0,0,.15)">
  <svg class="abs" style="left:0;top:0" width="180" height="161" viewBox="0 0 180 161" aria-hidden="true"><rect x="130" y="20" width="50" height="120" fill="#cfcfcf"/><polygon points="0,0 135,0 107,161 0,161" fill="#f37122"/></svg>
  <div class="abs chairs-label" style="left:15px;top:36px">CHAIRS<br><span style="font-size:22px">+</span><br>MORE</div>
</div>
<div class="abs product" style="left:613px;top:984px;background:radial-gradient(circle at 50% 35%,#d8d6d2,#f0f0ee 60%,#fafafa)" role="img" aria-label="Photo of a round clock-face side table on a dark pedestal"></div>
<div class="abs product" style="left:817px;top:984px;background:linear-gradient(160deg,#b04a3a,#6a1f20 50%,#2b1414)" role="img" aria-label="Photo of a red-lit lounge interior with banquette seating"></div>

<div class="abs bag-btn" style="left:203px;top:1158px"><svg width="13" height="13" viewBox="0 0 13 13"><path d="M1 4h11l-1 9H2z" fill="#999"/><path d="M4 4a2.5 2.5 0 0 1 5 0" fill="none" stroke="#999"/></svg></div>
<div class="abs price" style="left:321px;top:1158px">$ 200.00</div>
<div class="abs bag-btn" style="left:408px;top:1158px"><svg width="13" height="13" viewBox="0 0 13 13"><path d="M1 4h11l-1 9H2z" fill="#999"/><path d="M4 4a2.5 2.5 0 0 1 5 0" fill="none" stroke="#999"/></svg></div>
<div class="abs price" style="left:526px;top:1158px">$ 200.00</div>
<div class="abs bag-btn" style="left:613px;top:1158px"><svg width="13" height="13" viewBox="0 0 13 13"><path d="M1 4h11l-1 9H2z" fill="#999"/><path d="M4 4a2.5 2.5 0 0 1 5 0" fill="none" stroke="#999"/></svg></div>
<div class="abs price" style="left:731px;top:1158px">$ 200.00</div>
<div class="abs bag-btn" style="left:817px;top:1158px"><svg width="13" height="13" viewBox="0 0 13 13"><path d="M1 4h11l-1 9H2z" fill="#999"/><path d="M4 4a2.5 2.5 0 0 1 5 0" fill="none" stroke="#999"/></svg></div>
<div class="abs price" style="left:935px;top:1158px">$ 200.00</div>

<!-- products row 2 -->
<div class="abs product" style="left:203px;top:1231px;background:linear-gradient(180deg,#e6e6e6,#d8d8d8 45%,#3a3a3a 70%,#e4e4e4)" role="img" aria-label="Photo of a curved outdoor daybed with a black lattice frame and cushions"></div>
<div class="abs product" style="left:408px;top:1231px;background:linear-gradient(180deg,#eeeeee,#e6e6e6 40%,#2a6bb8 55%,#e8e8e8 75%)" role="img" aria-label="Photo of a blue upholstered chaise lounge on wooden legs"></div>
<div class="abs product" style="left:613px;top:1231px;background:linear-gradient(180deg,#ececec,#e8e8e8 35%,#233f7a 55%,#e6e6e6 80%)" role="img" aria-label="Photo of a navy blue sectional sofa with grey cushions"></div>
<div class="abs product" style="left:817px;top:1231px;background:radial-gradient(ellipse at 50% 50%,#8c7d5c,#e8e6e2 45%,#fff);box-shadow:0 1px 4px rgba(0,0,0,.12)" role="img" aria-label="Photo of a studded bronze side chair with a curved back"></div>

<div class="abs bag-btn" style="left:203px;top:1403px"><svg width="13" height="13" viewBox="0 0 13 13"><path d="M1 4h11l-1 9H2z" fill="#999"/><path d="M4 4a2.5 2.5 0 0 1 5 0" fill="none" stroke="#999"/></svg></div>
<div class="abs price" style="left:321px;top:1403px">$ 200.00</div>
<div class="abs bag-btn" style="left:408px;top:1403px"><svg width="13" height="13" viewBox="0 0 13 13"><path d="M1 4h11l-1 9H2z" fill="#999"/><path d="M4 4a2.5 2.5 0 0 1 5 0" fill="none" stroke="#999"/></svg></div>
<div class="abs price" style="left:526px;top:1403px">$ 200.00</div>
<div class="abs bag-btn" style="left:613px;top:1403px"><svg width="13" height="13" viewBox="0 0 13 13"><path d="M1 4h11l-1 9H2z" fill="#999"/><path d="M4 4a2.5 2.5 0 0 1 5 0" fill="none" stroke="#999"/></svg></div>
<div class="abs price" style="left:731px;top:1403px">$ 200.00</div>
<div class="abs bag-btn" style="left:817px;top:1403px"><svg width="13" height="13" viewBox="0 0 13 13"><path d="M1 4h11l-1 9H2z" fill="#999"/><path d="M4 4a2.5 2.5 0 0 1 5 0" fill="none" stroke="#999"/></svg></div>
<div class="abs price" style="left:935px;top:1403px">$ 200.00</div>

<!-- profile -->
<svg class="abs portrait" viewBox="0 0 310 348" role="img" aria-label="Black and white portrait photo of the principal designer">
  <defs><linearGradient id="portraitTone" x1="0" y1="0" x2="1" y2="1"><stop offset="0" stop-color="#9a9a9a"/><stop offset=".5" stop-color="#5c5c5c"/><stop offset="1" stop-color="#d8d8d8"/></linearGradient></defs>
  <polygon points="0,0 310,0 125,348 0,348" fill="url(#portraitTone)"/>
</svg>
<h2 class="abs section-title" style="left:361px;top:1578px">About Lori Velasco</h2>
<p class="abs section-sub" style="left:362px;top:1627px">Lorivel Designs House</p>
<div class="abs card bio">As a child, Lori would spend quality time with her Father by helping out in his furniture manufacturing company. She was delighted to be taken along on project installations to exciting places like the Solenne and other high-end hotels. What began as a fun after-school activity evolved into a passion for furniture &amp; interior design and quality materials.</div>
<h2 class="abs section-title" style="left:820px;top:1578px">Interior Design</h2>
<p class="abs section-sub" style="left:821px;top:1627px">Lorivel Designs House</p>
<div class="abs card design-card"></div>
<div class="abs design-btn" style="top:1702px;background:var(--blue)">COMMERCIAL DESIGN</div>
<div class="abs design-btn" style="top:1752px;background:var(--orange)">RESIDENTIAL DESIGN</div>

<!-- press -->
<section class="abs press"></section>
<p class="abs press-copy">Lorem ipsum dolor sit amet, consectetur adipiscing elit, sed do eiusmod tempor incididunt ut labore et dolore magna aliqua. Ut enim ad minim veniam, quis nostrud exercitation ullamco laboris nisi ut aliquip ex ea commodo consequat. Duis aute irure dolor in reprehenderit in voluptate velit esse cillum dolore eu fugiat nulla pariatur. Excepteur sint occaecat cupidatat non proident, sunt in culpa qui officia deserunt mollit anim id est laborum.</p>
<p class="abs press-date">16 APRIL 2018</p>
<div class="abs press-btn">MORE ARTICLES</div>

<!-- footer -->
<footer class="abs footer"></footer>
<h4 class="abs foot-head" style="left:163px">QUICK LINKS</h4>
<ul class="abs foot-links" style="left:163px"><li class="current">Home</li><li>About</li><li>Services</li><li>Shop</li></ul>
<ul class="abs foot-links" style="left:283px"><li>Contact</li><li>Blog</li></ul>
<h4 class="abs foot-head" style="left:483px">SIGNUP OUR NEWSLETTER</h4>
<div class="abs news-input"></div>
<div class="abs news-submit">SUBMIT</div>
<h4 class="abs foot-head" style="left:738px">EVENTS</h4>
<p class="abs event"><b>13 April 2018</b> dolor sit amet, consectetur adipiscing elit, sed do eiusmod tempor incididunt ut labore et dolore magna aliqua. sed do eiusmod tempor incididunt ut labore et dolore</p>
<div class="abs foot-rule"></div>
<p class="abs copyright">© Copyright 2018 Lorivel Designs. All Rights Reserved.</p>
<div class="abs social" style="left:947px;background:#3b5a9a"></div>
<div class="abs social" style="left:979px;background:#2aa3e0"></div>
<div class="abs social" style="left:1012px;background:#1a78b4"></div>

</body>
</html>
```